Defense contractor needs a roll-up for an exhibition

The booth we have booked has only a size of 3m².
So this will be the centerpiece of the whole booth.
We need a roll-up that attracts visitors and at the same time it should contain already designed graphics. These graphics are giving visitors an overview of our system. So it is necessary to have them exposed in a height that the booth personal can conveniently point with its fingers at them.
For information about our company and product visit:
https://www.brightlanternoptics.com/
For designing you should use Adobe Illustrator and the templates provided in the zip file, to guarantee a perfect print.
I have supplied my business card that you can copy the logo. As the company logo will be already at the booth nearby the top of the roll-up, you should not place it there. It can be in the middle or at the bottom.
I have uploaded a picture of the booth. The roll up will be placed at the left of the screen and has a size of 80cm x 200cm

Defense

Defense

Serif

Colors
0054AA
0677BA
7BADD7
CADEEF
E8F1F8

• you must use the Adobe Illustrator template to have a good printing result
• company logo on the upper side of the roll-up

```html
<!DOCTYPE html>
<html lang="en">
<head>
<meta charset="utf-8">
<title>Combat Training Systems Roll-up</title>
<link href="https://fonts.googleapis.com/css2?family=Anton&family=Lora:ital,wght@0,400;0,500;1,500&display=swap" rel="stylesheet">
<style>
  :root {
    --page-bg: #a3a3a3;
    --ink-black: #000000;
    --brand-deep: #0054aa;
    --brand-mid: #0677ba;
    --brand-sky: #7badd7;
    --brand-pale: #cadeef;
    --brand-mist: #e8f1f8;
    --circle-light: #eceef8;
    --circle-shade: #d4d8ea;
    --sunset-rose: #d9849a;
    --sunset-amber: #f0a070;
    --sunset-violet: #5b5fa8;
    --white: #ffffff;
  }
  * { margin: 0; padding: 0; box-sizing: border-box; }
  html, body { width: 807px; height: 1200px; overflow: hidden; background: var(--page-bg); }

  .rollup {
    position: absolute; left: 163px; top: 0; width: 480px; height: 1200px;
    background: var(--ink-black); overflow: hidden;
  }

  /* Sunset sky with the tank silhouette standing in the dark lower half */
  .hero-scene {
    position: absolute; left: 0; top: 0; width: 480px; height: 192px;
    background:
      radial-gradient(ellipse 62% 34% at 46% 70%, rgba(0,0,0,0.95) 0%, rgba(0,0,0,0.85) 60%, rgba(0,0,0,0) 100%),
      linear-gradient(180deg, rgba(0,0,0,0) 0%, rgba(0,0,0,0) 58%, rgba(0,0,0,0.9) 82%, #000 100%),
      linear-gradient(168deg, var(--sunset-violet) 0%, var(--sunset-rose) 26%, var(--sunset-amber) 40%, #b98fb6 55%, #6f72b8 72%, #3f4c9c 100%);
  }

  .headline {
    position: absolute; left: 0; width: 480px; text-align: center;
    font-family: "Anton", sans-serif; transform: skewX(-10deg);
  }
  .headline-main {
    top: 190px; font-size: 64px; line-height: 1; color: var(--brand-deep);
    -webkit-text-stroke: 1.5px var(--white); letter-spacing: -1px;
  }
  .headline-sub { color: var(--white); font-size: 23px; line-height: 1; letter-spacing: 0.3px; }
  .headline-sub.one { top: 263px; }
  .headline-sub.two { top: 298px; }

  .feature-band { position: absolute; left: 0; top: 0; width: 480px; height: 1200px; }

  .visual-circle {
    position: absolute; border-radius: 50%;
    border: 7px solid var(--white);
  }
  .visual-circle.range-view {
    left: 141px; top: 333px; width: 445px; height: 445px;
    background: radial-gradient(circle at 40% 40%, var(--circle-light) 0%, var(--brand-mist) 45%, var(--circle-shade) 100%);
  }
  .visual-circle.classroom-view {
    left: -8px; top: 496px; width: 290px; height: 290px;
    background: radial-gradient(circle at 55% 45%, var(--circle-light) 0%, var(--brand-mist) 40%, var(--circle-shade) 100%);
  }

  .product-name {
    position: absolute; left: 0; top: 790px; width: 480px; text-align: center;
    font-family: "Lora", serif; color: var(--white); font-size: 46px; font-weight: 500; line-height: 1.1;
  }
  .product-expansion {
    position: absolute; left: 0; top: 852px; width: 480px; text-align: center;
    font-family: "Lora", serif; color: var(--white); font-size: 23px; line-height: 1.2;
  }

  .feature-list {
    position: absolute; list-style: none; font-family: "Lora", serif;
    color: var(--white); font-size: 12.5px; line-height: 1.2;
  }
  .feature-list li { position: relative; padding-left: 18px; margin-bottom: 8px; }
  .feature-list li::before { content: "»"; position: absolute; left: 0; top: -1px; }
  .feature-list.left { left: 22px; top: 944px; width: 215px; }
  .feature-list.right { left: 250px; top: 944px; width: 215px; }
  .feature-list.right li { margin-bottom: 10px; }

  .brand-mark {
    position: absolute; left: 0; top: 1133px; width: 480px; text-align: center;
    font-family: "Lora", serif; font-size: 28px; font-weight: 500; color: var(--white);
  }
</style>
</head>
<body>
  <main class="rollup">
    <div class="hero-scene" role="img" aria-label="Photograph: silhouette of a battle tank on grass against a sunset sky"></div>

    <h1 class="headline headline-main">ADVANCED</h1>
    <p class="headline headline-sub one">COMBAT TRAINING SYSTEMS</p>
    <p class="headline headline-sub two">FOR REALISTIC COMBAT SIMULATION</p>

    <svg class="feature-band" viewBox="0 0 480 1200" aria-hidden="true">
      <defs>
        <linearGradient id="bandBlue" x1="0" y1="0" x2="1" y2="1">
          <stop offset="0" stop-color="#0677ba"/>
          <stop offset="0.5" stop-color="#0054aa"/>
          <stop offset="1" stop-color="#0a5fb8"/>
        </linearGradient>
      </defs>
      <path d="M0 690 H480 V1010 C380 1075 200 1095 0 1060 Z" fill="url(#bandBlue)"/>
      <path d="M0 1060 C200 1095 380 1075 480 1010 L480 1030 C380 1092 200 1106 0 1070 Z" fill="#0a3f86"/>
      <path d="M40 1088 C230 1100 390 1065 480 1020 L480 1036 C390 1086 230 1112 40 1088 Z" fill="#ffffff"/>
    </svg>

    <div class="visual-circle range-view" role="img" aria-label="System illustration: tanks on a range, target stations and an instructor control truck with screens"></div>
    <div class="visual-circle classroom-view" role="img" aria-label="System illustration: instructor room with two wall screens and rows of workstations"></div>

    <h2 class="product-name">ORTIS</h2>
    <p class="product-expansion">(Optical Range Tracking And<br>Instrumentation System)</p>

    <ul class="feature-list left">
      <li>Remote-Control Functions</li>
      <li>16 Camera Systems per vehicle</li>
      <li>Optics Camera</li>
      <li>Vehicle Data</li>
    </ul>
    <ul class="feature-list right">
      <li>Full Instructor Overview with Audio, Visuals, Vehicle Data, and Camera Control</li>
      <li>Air-Conditioned Instructor Command Workstation</li>
    </ul>

    <p class="brand-mark">Bright Lantern Optics</p>
  </main>
</body>
</html>
```